Original catchy book cover

I need a book cover for my book "The Copper Kettle Handbook" (https://quillpress.example/copperkettle). This will be a book self published on marketvale.
The book talks about the following concepts:
- Iterative product delivery
- Early discovery using feedback from customers
- Start small, think big, move fast
- Slice the product into valuable increments that can be validated with customers
- Experimental approach to deciding the next slice of work
A simple cover that stands out from the business books already out there! Some examples are:
https://www.marketvale.example/Tide-Harbor-Steady-Teams-Quietly-ebook/dp/X00AAA1111/ref=sr_1_1?ie=UTF8&qid=1000000001&sr=8-1&keywords=tide+and+harbor
https://www.marketvale.example/Copper-Kettle-Almanac-Brew-Ideas-ebook/dp/X00BBB2222/ref=sr_1_1?s=digital-text&ie=UTF8&qid=1000000002&sr=1-1&keywords=copper+kettle+almanac
https://www.marketvale.example/Orchard-Paths-Rewoven-Compass-Fogbanks-ebook/dp/X00CCC3333/ref=pd_sim_351_2?_encoding=UTF8&psc=1&refRID=ZZZZZZZZZZZZZZZZZZZZ
Lastly, attached are 2 draft covers that i've been playing with. Would love a graphic as part of the cover if it makes sense in your design! The graphic should tie to the meaning or themes of the book. Emphasis on ways of working, collaboration, experimentation, hypothesis, agile, incremental or adaptive. Those are some words that describe the content of the book.
Alternatively, something abstract could also be an option if a literal graphic doesn't suit the theme of your design.
Target Market(s)
Product owners, scrum masters, people in the agile community, software developers, designers
Industry/Entity Type
Information Technology
Font styles to use
Colors
Designer to choose colors to be used in the design.
Requirements
Must have
- Title, Subtitle, Author Name
- Back of the book should have space for a description (use lorem ipsum for now)
- Please use the editorial logo
- (please omit "created by Tomas Verhelst" because the editorial logo replaces that.
- The design must be original art or graphics (i.e. it should be similar to another cover in this topic).
Nice to have
- A graphic would be ideal if it is relevant to the book topic, otherwise a nice simple cover that uses colors or patterns that are easy to recall.
- The color suggestions below are suggestions only. Do not feel you have to incorporate all the colors and feel free to recommend an alternate palette.
Should not have
- Clipart or generic stock art photos. Images for the sake of images, traditional logos (e.g. a computer, a phone etc unless it's part of an overall theme that ties the logos together).

```html
<!DOCTYPE html>
<html lang="en">
<head>
<meta charset="utf-8">
<title>The Copper Kettle Handbook — Cover Spread</title>
<link href="https://fonts.googleapis.com/css2?family=Montserrat:wght@500;600;700;800&family=Open+Sans:wght@400;600&display=swap" rel="stylesheet">
<style>
  :root {
    --page: #ffffff;
    --pink-top: #ee3186;
    --pink-mid: #ea1b55;
    --pink-deep: #cc1748;
    --spine: #d9184c;
    --yellow: #f8ec3a;
    --white: #ffffff;
    --ink: #2f2f33;
    --photo: #414143;
    --art-light: #ffffff;
    --art-pink: #f43f7a;
  }
  * { box-sizing: border-box; margin: 0; padding: 0; }
  html, body { width: 1200px; height: 1200px; overflow: hidden; background: var(--page); }
  .canvas { position: relative; width: 1200px; height: 1200px; }

  .spread {
    position: absolute; left: 100px; top: 264px; width: 1001px; height: 673px;
    display: flex;
    font-family: "Montserrat", sans-serif;
    color: var(--white);
  }
  .panel { position: relative; height: 100%; overflow: hidden; }

  /* Back cover */
  .back {
    width: 454px;
    background: linear-gradient(160deg, var(--pink-mid) 0%, var(--pink-top) 45%, var(--pink-mid) 75%, var(--pink-deep) 100%);
  }
  .back .title-block { position: absolute; top: 40px; left: 0; width: 100%; text-align: center; }
  .back .title-small { font-weight: 600; font-size: 19px; letter-spacing: 4px; }
  .back .title-accent { font-weight: 700; font-size: 40px; color: var(--yellow); line-height: 1.1; letter-spacing: -0.5px; }
  .back .title-main { font-weight: 700; font-size: 34px; line-height: 1.1; letter-spacing: -0.5px; }

  .description {
    position: absolute; left: 46px; top: 174px; width: 367px;
    font-family: "Open Sans", sans-serif; font-size: 10.6px; line-height: 13.2px;
    text-align: justify;
  }
  .description p { text-indent: 20px; }

  .author-band {
    position: absolute; left: 0; top: 410px; width: 100%; height: 164px;
    background: var(--white); color: var(--ink);
  }
  .author-photo { position: absolute; left: 46px; top: 38px; width: 87px; height: 102px; background: var(--photo); }
  .author-band .author-name {
    position: absolute; left: 160px; top: 12px;
    font-weight: 600; font-size: 22px; letter-spacing: 2.5px;
  }
  .author-bio {
    position: absolute; left: 160px; top: 50px; width: 253px;
    font-family: "Open Sans", sans-serif; font-size: 10.6px; line-height: 13.2px; text-align: justify;
  }
  .author-bio p { text-indent: 20px; }

  .back-footer { position: absolute; left: 0; top: 574px; width: 100%; height: 99px; background: var(--pink-deep); }
  .barcode-space { position: absolute; left: 304px; top: 12px; width: 109px; height: 67px; border: 1px solid var(--white); background: var(--pink-mid); }

  .imprint { position: absolute; display: flex; align-items: center; gap: 10px; }
  .imprint .mark { border-radius: 50%; border: 4px solid var(--white); }
  .imprint .name { font-weight: 500; line-height: 1.05; }
  .imprint .url { display: block; font-weight: 600; }
  .back-footer .imprint { left: 46px; top: 18px; }
  .back-footer .imprint .mark { width: 52px; height: 52px; }
  .back-footer .imprint .name { font-size: 18px; }
  .back-footer .imprint .url { font-size: 13px; margin-top: 3px; }

  /* Spine */
  .spine { width: 92px; background: linear-gradient(180deg, var(--pink-mid), var(--spine) 60%, var(--pink-deep)); }
  .spine-text {
    position: absolute; left: 50%; top: 50%;
    width: 633px; height: 40px;
    transform: translate(-50%, -50%) rotate(-90deg);
    white-space: nowrap;
    display: flex; align-items: center; justify-content: space-between;
  }
  .spine-author { font-weight: 600; font-size: 21px; letter-spacing: 2px; }
  .spine-title { font-weight: 700; font-size: 21px; color: var(--yellow); }

  /* Front cover */
  .front {
    width: 455px;
    background: linear-gradient(165deg, var(--pink-top) 0%, var(--pink-mid) 40%, var(--pink-mid) 70%, var(--pink-deep) 100%);
    text-align: center;
  }
  .front .title-small { position: absolute; top: 38px; width: 100%; font-weight: 700; font-size: 32px; letter-spacing: 7px; }
  .front .title-accent { position: absolute; top: 80px; width: 100%; font-weight: 700; font-size: 78px; line-height: 1; color: var(--yellow); letter-spacing: -1px; }
  .front .title-main { position: absolute; top: 170px; width: 100%; font-weight: 700; font-size: 60px; line-height: 1; letter-spacing: -1px; }
  .subtitle { position: absolute; top: 262px; width: 100%; font-weight: 600; font-size: 15.5px; line-height: 16px; letter-spacing: 0.5px; }
  .front .author-name { position: absolute; top: 312px; width: 100%; font-weight: 600; font-size: 27px; letter-spacing: 3px; color: var(--yellow); }

  .cover-art {
    position: absolute; left: 110px; top: 352px; width: 234px; height: 236px;
    border-radius: 117px 117px 40px 40px;
    background: radial-gradient(circle at 50% 55%, var(--art-light) 0%, var(--art-light) 55%, var(--art-pink) 100%);
  }
  .front .imprint { left: 180px; top: 610px; gap: 8px; text-align: left; }
  .front .imprint .mark { width: 38px; height: 38px; border-width: 3px; }
  .front .imprint .name { font-size: 13px; }
  .front .imprint .url { font-size: 9px; margin-top: 2px; }
</style>
</head>
<body>
<div class="canvas">
  <div class="spread">

    <section class="panel back">
      <div class="title-block">
        <div class="title-small">THE COPPER</div>
        <div class="title-accent">KETTLE</div>
        <div class="title-main">HANDBOOK</div>
      </div>
      <div class="description">
        <p>Lorem ipsum dolor sit amet, consectetur adipiscing elit. Proin molestie, eros et vehicula consequat, augue mauris porttitor orci, vel tincidunt est felis at lectus. Integer euismod molestie arcu, vitae cursus nunc faucibus vel. Donec gravida iaculis sem sit amet tincidunt. Nam placerat, lectus eu maximus faucibus, lectus lectus tincidunt lectus, ut posuere ipsum eros id nibh. Etiam laoreet, nunc ac egestas tempus, lectus ante tincidunt nunc, a laoreet ex erat vitae justo.</p>
        <p>Fusce gravida felis at semper sagittis. Fusce rutrum vel augue quis posuere. Curabitur non mi eu libero porta tempus in sed mauris. Aliquam tristique iaculis lacus, ac scelerisque odio egestas sit amet. Vestibulum dapibus gravida mi, sed semper turpis tristique maximus. Aenean viverra odio ligula, sed rhoncus ex tempus ac. Suspendisse varius dapibus pellentesque. Fusce sollicitudin mattis ipsum, eget consequat velit faucibus eu.</p>
      </div>
      <div class="author-band">
        <div class="author-photo" role="img" aria-label="Author portrait placeholder"></div>
        <div class="author-name">MARA OKONJO</div>
        <div class="author-bio">
          <p>Lorem ipsum dolor sit amet, consectetur adipiscing elit. Proin molestie, eros et vehicula consequat, augue mauris porttitor orci, vel tincidunt est felis at lectus. Integer euismod molestie arcu, vitae cursus nunc faucibus vel. Donec gravida iaculis sem sit amet tincidunt.</p>
        </div>
      </div>
      <div class="back-footer">
        <div class="imprint">
          <span class="mark"></span>
          <span class="name">Editora<br>Brisa<span class="url">brisa.example</span></span>
        </div>
        <div class="barcode-space"></div>
      </div>
    </section>

    <section class="panel spine">
      <div class="spine-text">
        <span class="spine-author">MARA OKONJO</span>
        <span class="spine-title">THE COPPER KETTLE HANDBOOK</span>
      </div>
    </section>

    <section class="panel front">
      <div class="title-small">THE COPPER</div>
      <div class="title-accent">KETTLE</div>
      <div class="title-main">HANDBOOK</div>
      <div class="subtitle">A practitioner’s guide to building viable<br>products customers love</div>
      <div class="author-name">MARA OKONJO</div>
      <div class="cover-art" role="img" aria-label="Illustration of a teal light bulb launching like a rocket from pink clouds against a white circle"></div>
      <div class="imprint">
        <span class="mark"></span>
        <span class="name">Editora<br>Brisa<span class="url">brisa.example</span></span>
      </div>
    </section>

  </div>
</div>
</body>
</html>
```